Modern Business Card

Modern professional business card with more than just logo and demographic info. Something memorable.

We are a trendy/modern chiropractic group with an emphasis on neurology, hence the minimalist-type brain logo. We want to convey that modern and technical aspect with professionalism and the elite nature of our practice environment.

```html
<!DOCTYPE html>
<html lang="en">
<head>
<meta charset="utf-8">
<title>Meridian Spine Studio – Business Card</title>
<link href="https://fonts.googleapis.com/css2?family=Open+Sans:wght@400;600;700&display=swap" rel="stylesheet">
<style>
  :root {
    --backdrop: #2f2925;
    --card: #262627;
    --card-back: #1f1f20;
    --emboss: #2c2c2e;
    --blue: #3b78c4;
    --white: #f2f2f2;
    --muted: #d8d8d8;
  }
  * { box-sizing: border-box; margin: 0; padding: 0; }
  html, body {
    width: 1200px; height: 847px; overflow: hidden;
    background: var(--backdrop);
    font-family: "Open Sans", Arial, sans-serif;
  }
  .sheet {
    width: 1200px; height: 847px;
    display: flex; align-items: center; justify-content: center; gap: 40px;
  }
  .card {
    position: relative;
    width: 520px; height: 297px;
    background: var(--card);
    box-shadow: 0 10px 30px rgba(0,0,0,.45);
  }
  .card--back { background: var(--card-back); }

  .brand {
    position: absolute;
    display: flex; align-items: center; gap: 12px;
    font-weight: 600; text-transform: uppercase; letter-spacing: 1.5px;
    line-height: 1;
  }
  .brand__dot { width: 26px; height: 26px; border-radius: 50%; flex: none; }

  .card--back .brand { left: 0; right: 0; top: 130px; justify-content: center; font-size: 26px; color: var(--emboss); }
  .card--back .brand__dot { background: var(--emboss); }

  .card--front .brand { left: 180px; top: 82px; font-size: 22px; color: var(--white); }
  .card--front .brand__dot { background: var(--blue); }

  .holder {
    position: absolute; right: 280px; top: 196px;
    text-align: right; white-space: nowrap;
  }
  .holder__name { font-weight: 600; font-size: 17px; color: var(--blue); text-transform: uppercase; letter-spacing: .3px; }
  .holder__role { font-size: 13px; color: var(--muted); margin-top: 3px; }

  .divider {
    position: absolute; left: 254px; top: 190px;
    width: 1px; height: 62px; background: var(--blue);
  }

  .contacts {
    position: absolute; left: 266px; top: 188px;
    list-style: none; font-size: 13px; color: var(--white);
  }
  .contacts li { display: flex; align-items: center; gap: 6px; height: 22px; }
  .contacts svg { width: 11px; height: 11px; fill: var(--blue); flex: none; }
</style>
</head>
<body>
<main class="sheet">
  <section class="card card--back" aria-label="Card back">
    <div class="brand"><span class="brand__dot"></span>Meridian Spine Studio</div>
  </section>

  <section class="card card--front" aria-label="Card front">
    <div class="brand"><span class="brand__dot"></span>Meridian Spine Studio</div>

    <div class="holder">
      <p class="holder__name">Daniel Hartwell</p>
      <p class="holder__role">President</p>
    </div>

    <span class="divider"></span>

    <ul class="contacts">
      <li>
        <svg viewBox="0 0 24 24" aria-hidden="true"><path d="M6.6 10.8a15.1 15.1 0 0 0 6.6 6.6l2.2-2.2c.3-.3.7-.4 1-.2 1.1.4 2.3.6 3.6.6.6 0 1 .4 1 1V20c0 .6-.4 1-1 1A17 17 0 0 1 3 4c0-.6.4-1 1-1h3.5c.6 0 1 .4 1 1 0 1.3.2 2.5.6 3.6.1.3 0 .7-.2 1z"/></svg>
        555-014-2290
      </li>
      <li>
        <svg viewBox="0 0 24 24" aria-hidden="true"><path d="M2 5h20v14H2z M2 5l10 8 10-8" stroke="#262627" stroke-width="1.5"/></svg>
        dan@meridianspine.com
      </li>
      <li>
        <svg viewBox="0 0 24 24" aria-hidden="true"><circle cx="12" cy="12" r="10"/><path d="M2 12h20M12 2c3 3 3 17 0 20M12 2c-3 3-3 17 0 20" stroke="#262627" stroke-width="1.5" fill="none"/></svg>
        www.meridianspine.com
      </li>
    </ul>
  </section>
</main>
</body>
</html>
```